Corvanta Business cards template

We're looking for something modern and elegant. We are a reseller of technology (computers, datacenter, etc). Color theme would be "only" white with the incorporation of the blue that's present on our website (Corvanta.com) and logo file. We would like for the card to provide all the necessary info for the specific person (Phone#, fax#, email, name, website URL) . I'm attaching the logo file to this request. Please have it show Montreal/New York somewhere, without providing specific addresses.

Target Market(s)

All b2b

Industry/Entity Type

Business

Contact Information for Business Card

Please have the color scheme be represented by only the white and blue from our website (Corvanta.com) and logo. We would like to logo on the card, but not big and overwhelming. This card will be used as a template for anybody within the company, it should display the user's name, phone#, fax#, email, job title and website URL. Please have it show Montreal/New York somewhere, without providing our specific addresses. Really, we're looking for a clean, simple and elegant look.

Font styles to use
Serif

Requirements
Must have
• Please see card details
Nice to have
• Please see card details
Should not have
• Anything tacky or tagline.

```html
<!DOCTYPE html>
<html lang="en">
<head>
<meta charset="utf-8">
<title>Corvanta Business Cards</title>
<link rel="stylesheet" href="https://fonts.googleapis.com/css2?family=Roboto:wght@400;700&display=swap">
<style>
  :root {
    --page-bg: #ebebeb;
    --brand-blue: #0a6fb8;
    --brand-blue-deep: #0866ab;
    --card-white: #f4f4f4;
    --accent-dark: #3a3d42;
    --text-white: #ffffff;
    --text-soft: #e6f0f8;
  }
  * { margin: 0; padding: 0; box-sizing: border-box; }
  html, body {
    width: 1200px;
    height: 576px;
    overflow: hidden;
    background: var(--page-bg);
    font-family: "Roboto", Arial, sans-serif;
  }
  .canvas {
    position: relative;
    width: 1200px;
    height: 576px;
  }
  .card {
    position: absolute;
    border-radius: 13px;
    overflow: hidden;
    background: linear-gradient(180deg, var(--brand-blue) 0%, var(--brand-blue-deep) 100%);
  }
  .card-front {
    left: 82px;
    top: 139px;
    width: 484px;
    height: 293px;
    display: flex;
    align-items: center;
    justify-content: center;
  }
  .front-wordmark {
    color: var(--text-white);
    font-weight: 400;
    font-size: 54px;
    letter-spacing: 0.5px;
    margin-top: -6px;
  }
  .card-back {
    left: 602px;
    top: 138px;
    width: 481px;
    height: 291px;
  }
  .back-shapes {
    position: absolute;
    inset: 0;
  }
  .holder {
    position: absolute;
    left: 34px;
    top: 33px;
    color: var(--text-white);
  }
  .holder-name {
    font-weight: 700;
    font-size: 18px;
    letter-spacing: 0.3px;
  }
  .holder-title {
    font-size: 11px;
    margin-top: 5px;
    color: var(--text-soft);
  }
  .contact-list {
    position: absolute;
    left: 34px;
    top: 187px;
    list-style: none;
    color: var(--text-white);
    font-size: 11.5px;
  }
  .contact-item {
    display: flex;
    align-items: center;
    height: 17px;
  }
  .contact-icon {
    width: 11px;
    height: 11px;
    margin-right: 12px;
    fill: var(--text-white);
  }
  .contact-cities {
    margin-top: 3px;
  }
  .back-wordmark {
    position: absolute;
    left: 404px;
    top: 146px;
    transform: translate(-50%, -50%) rotate(-90deg);
    color: var(--brand-blue);
    font-weight: 400;
    font-size: 40px;
    white-space: nowrap;
  }
</style>
</head>
<body>
<main class="canvas">
  <section class="card card-front">
    <span class="front-wordmark">Corvanta</span>
  </section>

  <section class="card card-back">
    <svg class="back-shapes" width="481" height="291" viewBox="0 0 481 291">
      <path d="M362 0 Q258 150 350 291 L481 291 L481 0 Z" fill="var(--card-white)"/>
      <path d="M372 0 L390 0 Q300 90 316 228 Q286 100 372 0 Z" fill="var(--accent-dark)"/>
    </svg>

    <div class="holder">
      <div class="holder-name">Daniel R. Hale</div>
      <div class="holder-title">Managing Director</div>
    </div>

    <ul class="contact-list">
      <li class="contact-item">
        <svg class="contact-icon" viewBox="0 0 12 12"><path d="M1 4 Q6 0 11 4 L9 5 L8 4 L4 4 L3 5 Z M3 6 L9 6 L10 11 L2 11 Z"/></svg>
        +1 555-014-2837
      </li>
      <li class="contact-item">
        <svg class="contact-icon" viewBox="0 0 12 12"><circle cx="6" cy="6" r="5" fill="none" stroke="#fff" stroke-width="1.2"/><path d="M1 6 H11 M6 1 Q3 6 6 11 M6 1 Q9 6 6 11" fill="none" stroke="#fff" stroke-width="1"/></svg>
        info@corvanta.com
      </li>
      <li class="contact-item">
        <svg class="contact-icon" viewBox="0 0 12 12"><rect x="0.5" y="2.5" width="11" height="7" fill="none" stroke="#fff" stroke-width="1.2"/><path d="M0.5 2.5 L6 7 L11.5 2.5" fill="none" stroke="#fff" stroke-width="1.2"/></svg>
        www.corvanta.com
      </li>
      <li class="contact-item contact-cities">Halden&nbsp; |&nbsp; Brookvale</li>
    </ul>

    <span class="back-wordmark">Corvanta</span>
  </section>
</main>
</body>
</html>
```